Marrowby's Vacation Rentals Business Card

Multi Million dollar villa rentals in the Dominican Republic.

Industry/Entity Type

Business

Contact Information for Business Card

I am looking for a high-end look around my company name/logo (see attached) on one side incorporating the following info: first and last name, title, address, phone #, email and company website. On the backside I want to add a full color picture of one of our villas (see attached).

```html
<!DOCTYPE html>
<html lang="en">
<head>
<meta charset="utf-8">
<title>Marrowby's Vacation Rentals – Business Card</title>
<link rel="stylesheet" href="https://fonts.googleapis.com/css2?family=Michroma&display=swap">
<style>
  :root {
    --page: #5a5a5a;
    --ink: #05050a;
    --paper: #ffffff;
    --gold: #f7a823;
    --ember: #ef5a24;
    --amber: #f7931e;
    --sky: #3f7fc4;
    --pool: #0f55a8;
  }
  * { margin: 0; padding: 0; box-sizing: border-box; }
  html, body { width: 1200px; height: 1200px; overflow: hidden; }
  body {
    background: var(--page);
    font-family: "Michroma", sans-serif;
    font-variant: small-caps;
    position: relative;
  }
  .card {
    position: absolute;
    left: 241px;
    width: 718px;
    height: 407px;
    overflow: hidden;
    box-shadow: 0 4px 10px rgba(0,0,0,.45);
  }
  .card--back { top: 170px; background: var(--ink); }
  .card--front { top: 624px; background: var(--paper); }

  .villa-photo {
    position: absolute; left: 0; top: 0; width: 718px; height: 292px;
    background: linear-gradient(180deg, var(--sky) 0%, #9cc0de 16%, #e9ece8 38%, #d7d5cc 62%, #6d7c6b 78%, var(--pool) 90%, var(--ink) 100%);
  }

  .brand { position: absolute; display: flex; align-items: center; gap: 10px; white-space: nowrap; }
  .brand__dot { border-radius: 50%; background: var(--amber); flex: none; }
  .brand__name { line-height: 1.15; }
  .card--back .brand { left: 26px; top: 318px; color: var(--paper); }
  .card--back .brand__dot { width: 34px; height: 34px; }
  .card--back .brand__name { font-size: 19px; }
  .card--front .brand { left: 26px; top: 22px; color: var(--ink); }
  .card--front .brand__dot { width: 48px; height: 48px; }
  .card--front .brand__name { font-size: 25px; }

  .back-contact { position: absolute; right: 31px; top: 326px; text-align: right; white-space: nowrap; }
  .back-contact__phone { color: var(--paper); font-size: 20px; letter-spacing: 2px; }
  .back-contact__web { color: var(--gold); font-size: 11px; letter-spacing: 3px; margin-top: 6px; }

  .swoosh { position: absolute; left: 0; top: 0; }

  .details { position: absolute; right: 31px; top: 164px; text-align: right; color: var(--paper); white-space: nowrap; }
  .details__name { color: var(--gold); font-size: 19px; letter-spacing: 3px; }
  .details__title { font-size: 12px; letter-spacing: 2px; margin-top: 6px; }
  .details__lines { margin-top: 22px; }
  .details__line { display: flex; justify-content: flex-end; align-items: center; gap: 8px; font-size: 12px; letter-spacing: 2.6px; height: 25px; }
  .details__line--phone { font-size: 15px; letter-spacing: 2px; }
  .details__line svg { width: 16px; height: 16px; flex: none; }
  .details__address { margin-top: 16px; font-size: 13px; letter-spacing: 3px; line-height: 24px; }
</style>
</head>
<body>

<section class="card card--back">
  <div class="villa-photo" role="img" aria-label="Photograph of a white two-storey villa with terracotta roof, arched veranda, palms and blue loungers beside a pool"></div>
  <div class="brand">
    <span class="brand__dot"></span>
    <span class="brand__name">Marrowby's<br>Vacation Rentals</span>
  </div>
  <div class="back-contact">
    <div class="back-contact__phone">+0 555-019-284</div>
    <div class="back-contact__web">www.marrowbysvacrent.com</div>
  </div>
</section>

<section class="card card--front">
  <svg class="swoosh" width="718" height="407" viewBox="0 0 718 407" aria-hidden="true">
    <path d="M460,0 C438,110 400,165 320,192" fill="none" stroke="var(--ember)" stroke-width="9"/>
    <path d="M320,192 C190,235 100,320 60,407" fill="none" stroke="var(--amber)" stroke-width="10"/>
    <path d="M474,0 C452,120 410,172 335,200 C215,245 122,318 86,407 L718,407 L718,0 Z" fill="var(--ink)"/>
  </svg>
  <div class="brand">
    <span class="brand__dot"></span>
    <span class="brand__name">Marrowby's<br>Vacation Rentals</span>
  </div>
  <div class="details">
    <div class="details__name">Daniel Reyes</div>
    <div class="details__title">Managing Partner</div>
    <div class="details__lines">
      <div class="details__line details__line--phone">+0 555-019-284
        <svg viewBox="0 0 16 16"><path d="M2 6 C2 3 14 3 14 6 L12 7 L10 5.5 L6 5.5 L4 7 Z M4 8 L12 8 L13 14 L3 14 Z" fill="var(--ember)"/><circle cx="8" cy="11" r="1.6" fill="var(--ink)"/></svg>
      </div>
      <div class="details__line">dreyes@marrowbysvacrent.com
        <svg viewBox="0 0 16 16"><rect x="1" y="3" width="14" height="10" fill="var(--ember)"/><path d="M1 3 L8 9 L15 3 M1 13 L6 8 M15 13 L10 8" fill="none" stroke="var(--ink)" stroke-width="1.2"/></svg>
      </div>
      <div class="details__line">www.marrowbysvacrent.com
        <svg viewBox="0 0 16 16" fill="none" stroke="var(--ember)" stroke-width="1.2"><circle cx="8" cy="8" r="6.5"/><ellipse cx="8" cy="8" rx="3" ry="6.5"/><path d="M1.5 8 H14.5 M2.5 4.8 H13.5 M2.5 11.2 H13.5"/></svg>
      </div>
    </div>
    <div class="details__address">1718 Willowmere Court<br>Brookfield, WI 53045</div>
  </div>
</section>

</body>
</html>
```